Gym Poster to advertise for our chiropractic business

We are needing a poster for a gym. They are a weight training gym, Copperline Gym. The poster will be 4 ft by 8 ft. This poster will be used for advertising purposes.
Target Market(s)
Athletes, 25 to 45,Men and Women,
Industry/Entity Type
Advertising
Font styles to use
Serif
Sans Serif

```html
<!DOCTYPE html>
<html lang="en">
<head>
<meta charset="utf-8">
<title>Ironside Chiropractic – Copperline Gym Poster</title>
<link href="https://fonts.googleapis.com/css2?family=Arimo:wght@400;700&display=swap" rel="stylesheet">
<style>
  :root {
    --panel-blue: #86aed0;
    --text-white: #ffffff;
    --brand-navy: #1f3a5c;
    --skin-light: #e9cdb6;
    --skin-mid: #d9ab8c;
    --sheet-white: #f3f1ee;
  }
  * { margin: 0; padding: 0; box-sizing: border-box; }
  html, body { width: 1200px; height: 2561px; overflow: hidden; }
  body { font-family: "Arimo", Arial, sans-serif; background: var(--panel-blue); }
  .poster { position: relative; width: 1200px; height: 2561px; background: var(--panel-blue); color: var(--text-white); }
  .hero-photo {
    position: absolute; left: 0; top: 0; width: 1200px; height: 814px;
    background: linear-gradient(160deg, var(--sheet-white) 0%, var(--skin-light) 35%, var(--skin-mid) 65%, var(--sheet-white) 100%);
  }
  .brand {
    position: absolute; left: 28px; top: 570px; display: flex; align-items: center; gap: 24px;
  }
  .brand-mark { width: 200px; height: 200px; }
  .brand-name {
    color: var(--brand-navy); font-weight: 700; font-size: 44px; line-height: 1.2;
  }
  .headline {
    position: absolute; top: 890px; left: 0; width: 1200px; text-align: center;
    font-size: 52px; line-height: 1.16; letter-spacing: 1px;
  }
  .headline strong { font-weight: 700; }
  .services {
    position: absolute; top: 1150px; left: 0; width: 1200px; text-align: center;
    font-weight: 700; list-style: none;
  }
  .services-title { font-size: 40px; margin-bottom: 22px; }
  .services li { font-size: 42px; line-height: 69.5px; letter-spacing: 0.5px; }
  .testimonial { position: absolute; font-size: 24px; line-height: 1.25; }
  .testimonial-left { left: 103px; top: 1968px; width: 470px; }
  .testimonial-right { left: 640px; top: 1968px; width: 460px; }
  .attribution { display: block; text-align: right; margin-top: 8px; }
  .testimonial-left .attribution { margin-top: 40px; padding-right: 15px; }
  .cta {
    position: absolute; top: 2290px; left: 0; width: 1200px; text-align: center; font-size: 52px; letter-spacing: 1px;
  }
  .website {
    position: absolute; top: 2377px; left: 0; width: 1200px; text-align: center; font-size: 30px; font-weight: 700; letter-spacing: 1px;
  }
  .contact {
    position: absolute; top: 2440px; left: 0; width: 1200px; text-align: center; font-size: 32px; letter-spacing: 1px;
  }
</style>
</head>
<body>
<div class="poster">
  <div class="hero-photo" role="img" aria-label="Photo of a chiropractor's hands pressing on a patient's lower back"></div>
  <div class="brand">
    <svg class="brand-mark" viewBox="0 0 200 200" aria-hidden="true">
      <circle cx="100" cy="100" r="94" fill="none" stroke="#1f3a5c" stroke-width="5"/>
    </svg>
    <div class="brand-name">Ironside<br>Chiropractic LLC</div>
  </div>

  <p class="headline">When <strong>YOU</strong> are suffering we offer the<br>best treatments and care available.</p>

  <ul class="services">
    <li class="services-title">Services:</li>
    <li>Chiropractic Adjustments</li>
    <li>Spinal Curve Correction</li>
    <li>Myofacial Release</li>
    <li>Massage Therapy</li>
    <li>Rehabilitation Services</li>
    <li>Strapping</li>
    <li>Sports Taping</li>
    <li>Orthotics and Bracing</li>
    <li>Supplementation</li>
  </ul>

  <blockquote class="testimonial testimonial-left">
    When I first came to Ironside my pain was unbearable. With the doctors and staff's help I was able to get my life back.
    <span class="attribution">- Maria</span>
  </blockquote>
  <blockquote class="testimonial testimonial-right">
    Warm, friendly office. The doctor answered all of my questions. Felt better the same day.
    <span class="attribution">- Drew</span>
  </blockquote>

  <p class="cta">We offer same day appointments!</p>
  <p class="website">www.alignwellcare.com</p>
  <p class="contact">2280 Harlow Avenue, Dallas, TX 75219 &nbsp;| Tel: 469.555.0188</p>
</div>
</body>
</html>
```